Concert Venue Show Posters (ongoing job too)

Looking for a designer for ongoing project to create posters for each of our concerts coming to the venue. We have a budget of $35-45.00 per poster and on average do 5-12 per month. We’re looking for simple, unique design template going forward as part of our branding.

We hope to establish a long term relationship with someone to do this work on an ongoing adhoc basis.

Goal is to simple tell folks who, where, and when.

Creative needs to delivered in Photoshop PSD file format in two sizes; 24" x 36" used onsite in lobby and 11" x 17" for offsite marketing distribution.

We’ll supply all approved artwork and information for you to use although sometimes what we get from management sucks.

You can look at some of our older posters here
http://bramblehallvenue.example-photos.com/Other/Posters/

Our website (it’s in re-design now)
http://www.bramblehallvenue.example

Our new website format moving toward this as template
http://www.copperlanternhall.example/event/252331-kestrel-owls-portland/

Thoughts? Ideas? Included artwork to see some samples.

Include these items on poster
Bramble HALL logo
Artists Name
Dorian Pike and the Lanterns (image with single guitar players)
Velvet Anchor (group image)
September 25, 2014
Doors 7:00
Show 8:00
You can sort of get an idea from our old posters.

PS this could lead to extra work doing our newspaper creatives too.
Updates

Project Deadline Extended
Reason: Due to weekend and workload of staff we'll make our final selection on Wednesday, August 28th by 6 PM EST. Thanks to everyone for submitting some great examples of work.

Target Market(s)

Onsite concert goers for future shows, and offsite spreading the word about shows.

Industry/Entity Type

Marketing

Requirements
Must have
• Simple is best. Not looking for bar band type posters, remember we're just letting fans know about who and when.
Nice to have
• Template, easy to reproduce show after show to keep costs down.
Should not have
• Less is more since we're just telling patons who, when, and where.

```html
<!DOCTYPE html>
<html lang="en">
<head>
<meta charset="utf-8">
<title>Dorian Pike and the Lanterns — Bramble HALL</title>
<link rel="stylesheet" href="https://fonts.googleapis.com/css2?family=Orbitron:wght@700;900&family=Archivo+Black&family=Old+Standard+TT&display=swap">
<style>
  :root {
    --ink: #ffffff;
    --night: #1b1512;
    --flame: #d9722a;
    --gold: #e6b24a;
    --badge: #c23a22;
  }
  html, body {
    margin: 0;
    padding: 0;
    width: 776px;
    height: 1200px;
    overflow: hidden;
    background: var(--night);
  }
  .poster {
    position: relative;
    width: 776px;
    height: 1200px;
    overflow: hidden;
    color: var(--ink);
  }
  .poster__art {
    position: absolute;
    inset: 0;
    background:
      radial-gradient(ellipse 60% 40% at 75% 60%, rgba(240,190,90,0.75), transparent 70%),
      radial-gradient(ellipse 50% 35% at 35% 25%, rgba(200,80,35,0.8), transparent 70%),
      linear-gradient(115deg, #151110 0%, #2a1a14 25%, #8a3a1e 45%, var(--flame) 65%, var(--gold) 85%, #9a8a70 100%);
  }
  .poster__art::after {
    content: "";
    position: absolute;
    inset: 0;
    background: linear-gradient(180deg, rgba(0,0,0,0) 55%, rgba(10,6,4,0.55) 100%);
  }
  .support {
    position: absolute;
    left: 26px;
    top: 12px;
    width: 198px;
    height: 198px;
    border-radius: 50%;
    background: var(--badge);
    border: 6px solid var(--ink);
    box-sizing: border-box;
    display: flex;
    align-items: center;
    justify-content: center;
    text-align: center;
    font-family: "Archivo Black", sans-serif;
    font-size: 26px;
    line-height: 1.1;
  }
  .venue {
    position: absolute;
    left: 292px;
    top: 18px;
    width: 210px;
    text-align center;
    font-family: "Archivo Black", sans-serif;
    line-height: 1;
  }
  .venue__top { font-size: 46px; }
  .venue__bottom { font-size: 90px; margin-top: 10px; }
  .present {
    position: absolute;
    left: 588px;
    top: 194px;
    font-family: "Archivo Black", sans-serif;
    font-size: 20px;
    letter-spacing: 2px;
  }
  .headliner {
    position: absolute;
    left: 40px;
    top: 466px;
    margin: 0;
    font-family: "Orbitron", sans-serif;
    font-weight: 900;
    font-size: 98px;
    line-height: 1;
    white-space: nowrap;
    transform: scaleY(2.05);
    transform-origin: left top;
    text-transform: uppercase;
  }
  .headliner__band {
    position: absolute;
    left: 50px;
    top: 680px;
    margin: 0;
    font-family: "Orbitron", sans-serif;
    font-weight: 700;
    font-size: 42px;
    line-height: 1;
    white-space: nowrap;
    transform: scaleY(1.9);
    transform-origin: left top;
    text-transform: uppercase;
  }
  .when {
    position: absolute;
    left: 0;
    width: 776px;
    display: flex;
    align-items: center;
    justify-content: center;
    gap: 12px;
  }
  .rule {
    display: block;
    height: 10px;
    border-top: 2px solid var(--ink);
    border-bottom: 2px solid var(--ink);
    box-sizing: border-box;
    width: 150px;
  }
  .when__day {
    top: 900px;
    font-family: "Old Standard TT", serif;
    font-size: 70px;
    line-height: 1;
  }
  .when__date {
    position: absolute;
    left: 0;
    top: 992px;
    width: 776px;
    text-align: center;
    font-family: "Archivo Black", sans-serif;
    font-size: 58px;
    letter-spacing: -1px;
    line-height: 1;
    white-space: nowrap;
    transform: scaleY(1.55);
    transform-origin: center top;
  }
  .when__doors {
    top: 1108px;
    font-family: "Old Standard TT", serif;
    font-size: 58px;
    line-height: 1;
  }
</style>
</head>
<body>
  <main class="poster">
    <div class="poster__art" role="img" aria-label="Photo of a long-haired guitarist playing an electric guitar against a warm orange and gold close-up of guitar pickups"></div>

    <div class="support">Velvet<br>Anchor</div>

    <div class="venue">
      <div class="venue__top">Bramble</div>
      <div class="venue__bottom">HALL</div>
    </div>

    <div class="present">PRESENT</div>

    <h1 class="headliner">Dorian Pike</h1>
    <h2 class="headliner__band">and the Lanterns</h2>

    <div class="when when__day"><span class="rule"></span><span>Wednesday</span><span class="rule"></span></div>
    <div class="when__date">SEPTEMBER 25, 2014</div>
    <div class="when when__doors"><span class="rule"></span><span>Doors at 7:00</span><span class="rule"></span></div>
  </main>
</body>
</html>
```